Business letterhead and powerpoint template

Hi, I have recently started using a new logo (found through PixelGrove) and would now like to use that logo for letterheads and powerpoint.

Attached is the logo and one version of a brochure I have recently used.

Industry/Entity Type

Business

```html
<!DOCTYPE html>
<html lang="en">
<head>
<meta charset="utf-8">
<title>Harlow Stationery</title>
<link href="https://fonts.googleapis.com/css2?family=Open+Sans:wght@300;400;600;700&display=swap" rel="stylesheet">
<style>
:root{
  --orange:#e2562b;
  --ink:#3a3a3a;
  --muted:#7a7a7a;
  --paper:#ffffff;
  --backdrop:#eeeeee;
  --rule:#dcdcdc;
}
*{box-sizing:border-box;margin:0;padding:0}
html,body{width:1200px;height:2400px;overflow:hidden}
body{background:var(--backdrop);font-family:'Open Sans',Arial,sans-serif;color:var(--ink);position:relative}
.sheet{position:absolute;background:var(--paper);box-shadow:0 2px 6px rgba(0,0,0,.12)}

/* brand wordmark */
.wordmark{font-weight:300;letter-spacing:.08em;color:var(--ink);display:flex;align-items:center;gap:.35em;line-height:1}
.wordmark .mark-square{display:inline-block;width:.8em;height:.8em;background:var(--orange)}

/* business card front */
.card-front{width:440px;height:252px;padding:30px 32px}
.card-front .wordmark{font-size:30px}
.card-front .social{position:absolute;top:34px;right:32px;display:flex;gap:6px}
.card-front .social span{width:14px;height:14px;background:#3b7dc4;border-radius:2px}
.card-name{font-size:17px;font-weight:700;margin-top:34px}
.card-role{font-size:10px;color:var(--muted);margin-bottom:10px}
.card-line{font-size:10px;color:var(--muted);display:flex;align-items:center;gap:7px;line-height:1.7}
.card-line .bullet{width:7px;height:7px;background:var(--orange);flex:none}

/* business card back */
.card-back{width:440px;height:252px;background:var(--orange);display:flex;align-items:center;justify-content:center}
.card-back .wordmark{font-size:54px;color:#f1f1f1;font-weight:300}

/* vertical card */
.card-vertical{width:252px;height:440px;padding:34px 26px}
.card-vertical .wordmark{font-size:30px}
.card-vertical .card-name{margin-top:40px}
.card-vertical .social{position:absolute;bottom:30px;right:26px;display:flex;gap:6px}
.card-vertical .social span{width:14px;height:14px;background:#3b7dc4;border-radius:2px}

/* letterhead */
.letterhead{width:500px;height:707px;padding:44px 46px}
.letterhead .wordmark{font-size:28px}
.letter-body{margin-top:36px;font-size:8.5px;line-height:1.7;color:#555}
.letter-body p{margin-bottom:9px}
.letter-body .subject{font-weight:700;color:var(--ink)}
.signature{width:110px;height:34px;margin:6px 0 4px;background:linear-gradient(90deg,#e6e6e6,#f4f4f4)}
.letter-footer{position:absolute;left:0;right:0;bottom:0}
.footer-row{display:flex;justify-content:space-between;align-items:center;padding:0 46px 8px;font-size:7px;color:var(--muted)}
.footer-row .footer-brand{font-size:14px}
.footer-rule{height:1px;background:var(--orange);margin:0 46px 8px}
.footer-band{height:12px;background:var(--orange)}

/* envelope */
.envelope{width:800px;height:400px;overflow:hidden}
.envelope-flap{position:absolute;left:0;right:0;top:0;height:170px;background:var(--orange);border-radius:0 0 14px 14px;display:flex;align-items:center;justify-content:center}
.envelope-flap .web{color:#fde3d9;font-size:13px;letter-spacing:.12em}
</style>
</head>
<body>

<!-- stationery set: business cards -->
<section class="sheet card-front" style="left:120px;top:120px">
  <div class="wordmark">HARLOW <span class="mark-square"></span></div>
  <div class="social"><span></span><span></span><span></span></div>
  <div class="card-name">Alex Morgan</div>
  <div class="card-role">Director</div>
  <div class="card-line"><span class="bullet"></span>Level 5, 12 Sample Street, Sydney NSW 2000 Australia</div>
  <div class="card-line"><span class="bullet"></span>+61 02 5550 0100</div>
  <div class="card-line"><span class="bullet"></span>alex@harlowcapital.example</div>
  <div class="card-line"><span class="bullet"></span>www.harlowcapital.example</div>
</section>

<section class="sheet card-back" style="left:640px;top:120px">
  <div class="wordmark">HARLOW</div>
</section>

<section class="sheet card-vertical" style="left:474px;top:420px">
  <div class="wordmark">HARLOW <span class="mark-square"></span></div>
  <div class="card-name">Alex Morgan</div>
  <div class="card-role">Director</div>
  <div class="card-line"><span class="bullet"></span>Level 5, 12 Sample Street</div>
  <div class="card-line"><span class="bullet"></span>Sydney NSW 2000 Australia</div>
  <div class="card-line"><span class="bullet"></span>+61 02 5550 0100</div>
  <div class="card-line"><span class="bullet"></span>www.harlowcapital.example</div>
  <div class="social"><span></span><span></span><span></span></div>
</section>

<!-- letterhead -->
<section class="sheet letterhead" style="left:160px;top:940px">
  <div class="wordmark">HARLOW <span class="mark-square"></span></div>
  <div class="letter-body">
    <p>29 June 2013<br>Recipient Name and Address Line</p>
    <p>Dear Mr/Ms Surname,</p>
    <p class="subject">Subject Matter Heading</p>
    <p>In this letter we outline the details of our proposal for you.<br>Please review the enclosed summary at your earliest convenience.</p>
    <p>The following points are set out for your attention.</p>
    <p>If you have any questions please feel free to contact us.</p>
    <p>Yours Sincerely,</p>
    <div class="signature" role="img" aria-label="Handwritten signature"></div>
  </div>
  <div class="letter-footer">
    <div class="footer-row">
      <span>+61 02 5550 0100</span>
      <span>info@harlowcapital.example</span>
      <span>www.harlowcapital.example</span>
      <span class="wordmark footer-brand">HARLOW</span>
    </div>
    <div class="footer-rule"></div>
    <div class="footer-band"></div>
  </div>
</section>

<section class="sheet card-back" style="left:740px;top:1080px;width:300px;height:172px">
  <div class="wordmark" style="font-size:38px">HARLOW</div>
</section>

<section class="sheet card-front" style="left:740px;top:1300px;width:300px;height:172px;padding:20px 22px">
  <div class="wordmark" style="font-size:20px">HARLOW <span class="mark-square"></span></div>
  <div class="social" style="top:22px;right:22px"><span style="width:10px;height:10px"></span><span style="width:10px;height:10px"></span></div>
  <div class="card-name" style="font-size:12px;margin-top:22px">Alex Morgan</div>
  <div class="card-role" style="font-size:8px;margin-bottom:6px">Director</div>
  <div class="card-line" style="font-size:8px"><span class="bullet"></span>+61 02 5550 0100</div>
  <div class="card-line" style="font-size:8px"><span class="bullet"></span>www.harlowcapital.example</div>
</section>

<!-- envelope -->
<section class="sheet envelope" style="left:200px;top:1860px">
  <div class="envelope-flap"><span class="web">www.harlowcapital.example</span></div>
</section>

</body>
</html>
```